Harborline Talent IT Recruiting firm needs a business card design for Recruiters, Sourcers, and Account

We need business cards that allow us to change all contact info, names, titles (Recruiter, Sourcer, Account Manager, Director, CEO, etc) per person since we have three offices, in three cities, Phoenix, Austin, and Las Vegas. We do recruiting and contractors for IT positions (Developers, Architects, Software Engineers, Security Engineers, Help Desk, DBAs, PMs, Scrum Masters, etc.) Our client companies are very diverse from Crestline 250 to silicone Valley type start-ups.

So, while we what hip, techie, and quirky, it still needs to be professional. Primary color we use is blue, with silver as a secondary color.

Target Market(s)

IT, Technology

Industry/Entity Type

Business

Contact Information for Business Card

Company name: Harborline Talent, Inc.
Website: www.harborlinetalent-example.com
Logos for ProCircle, Quillo, and Roomwall

Name, Title, Office Number, Cell Number, email

Font styles to use
Serif
Sans Serif

Colors
0455a3
d5d5d5

Requirements
Nice to have
• The grey I selected below is not necessary - but, would like silver included. I included a card design (File 3: HTI early trial example.jpg) that I had started on. It's very rough, and not quite what we're looking for, but what we did like is the logo, big, maybe a bit faded, off center, goes out of frame, etc. Still looking for other ideas - you are the pros! But, just an idea of a design element we liked.

```html
<!DOCTYPE html>
<html lang="en">
<head>
<meta charset="utf-8">
<title>Harborline Talent, Inc. — Business Card</title>
<link rel="stylesheet" href="https://fonts.googleapis.com/css2?family=Cormorant+Garamond:wght@400;500&family=Open+Sans:wght@400;600;800&display=swap">
<style>
  :root {
    --page: #e9e9ea;
    --blue-deep: #04527f;
    --blue: #0a7fb3;
    --blue-light: #1fa2d6;
    --brand-blue: #0455a3;
    --silver: #d5d5d5;
    --silver-light: #f1f1f2;
    --ink: #2f2f33;
    --white: #ffffff;
    --icon: #3a3f46;
  }
  html, body {
    margin: 0;
    width: 1200px;
    height: 1023px;
    overflow: hidden;
    background: var(--page);
  }
  .canvas {
    position: relative;
    width: 1200px;
    height: 1023px;
  }
  .card {
    position: absolute;
    width: 640px;
    height: 366px;
    overflow: hidden;
    border-radius: 3px;
    box-shadow: 0 10px 30px rgba(0,0,0,.18);
  }

  /* ---------- Front: blue contact side ---------- */
  .card-front {
    left: 80px;
    top: 90px;
    background: linear-gradient(150deg, var(--blue-light) 0%, var(--blue) 45%, var(--blue-deep) 100%);
    font-family: "Open Sans", sans-serif;
    color: var(--white);
  }
  .card-front .silver-bar {
    position: absolute;
    background: var(--silver);
  }
  .card-front .silver-bar.top { right: 0; top: 0; width: 16px; height: 130px; }
  .card-front .silver-bar.bottom { left: 0; bottom: 0; width: 16px; height: 120px; }
  .card-front .divider {
    position: absolute;
    left: 300px; top: 218px;
    width: 120px; height: 1px;
    background: linear-gradient(90deg, transparent, rgba(255,255,255,.7), transparent);
    transform: rotate(28deg);
  }
  .card-front .emblem-fade {
    position: absolute;
    right: -40px; top: -60px;
    width: 300px; height: 300px;
    border-radius: 50%;
    background: radial-gradient(circle, rgba(255,255,255,.16), rgba(255,255,255,.04) 70%);
  }
  .front-brand {
    position: absolute;
    right: 40px; top: 58px;
    text-align: right;
  }
  .front-brand .wordmark {
    display: flex; align-items: center; justify-content: flex-end; gap: 10px;
    font-family: "Cormorant Garamond", serif;
    font-weight: 500;
    font-size: 30px;
    letter-spacing: 3px;
    color: var(--ink);
    white-space: nowrap;
  }
  .front-brand .wordmark .dot {
    width: 22px; height: 22px; border-radius: 50%; background: var(--silver-light);
  }
  .front-brand .tagline {
    font-family: "Cormorant Garamond", serif;
    font-size: 11px; letter-spacing: 2px;
    color: var(--ink);
    margin-top: 4px;
  }
  .front-brand .company {
    font-weight: 800; font-size: 20px; margin-top: 14px;
  }
  .person {
    position: absolute;
    left: 40px; top: 170px;
  }
  .person .name { font-weight: 600; font-size: 24px; margin: 0; }
  .person .title { font-size: 13px; margin: 2px 0 10px; opacity: .85; }
  .contacts {
    list-style: none; margin: 0; padding: 0;
  }
  .contacts li {
    display: flex; align-items: center; gap: 10px;
    font-size: 13.5px; line-height: 21px;
  }
  .contacts .icon {
    width: 14px; height: 14px; flex: none;
    background: var(--icon);
    border-radius: 2px;
    display: flex; align-items: center; justify-content: center;
  }
  .contacts .icon svg { width: 10px; height: 10px; }

  /* ---------- Back: silver logo side ---------- */
  .card-back {
    left: 480px;
    top: 560px;
    background: linear-gradient(160deg, var(--white) 0%, var(--silver-light) 40%, var(--silver) 100%);
  }
  .card-back .emblem-fade {
    position: absolute;
    right: -90px; bottom: -120px;
    width: 330px; height: 330px;
    border-radius: 50%;
    background: radial-gradient(circle, rgba(10,127,179,.18), rgba(10,127,179,.05) 70%);
  }
  .back-brand {
    position: absolute;
    left: 50px; top: 80px;
  }
  .back-brand .wordmark {
    display: flex; align-items: center; gap: 12px;
    font-family: "Cormorant Garamond", serif;
    font-weight: 500;
    font-size: 36px;
    letter-spacing: 3px;
    color: var(--ink);
    line-height: 1;
    white-space: nowrap;
  }
  .back-brand .wordmark .dot {
    width: 40px; height: 40px; border-radius: 50%; flex: none;
    background: radial-gradient(circle at 40% 35%, var(--blue-light), var(--brand-blue));
  }
  .back-brand .tagline {
    font-family: "Cormorant Garamond", serif;
    font-size: 18px; letter-spacing: 4px;
    color: var(--ink);
    margin-top: 22px;
    white-space: nowrap;
  }
  .back-brand .company {
    font-family: "Open Sans", sans-serif;
    font-weight: 800; font-size: 32px;
    color: var(--brand-blue);
    margin-top: 10px;
    letter-spacing: .5px;
    white-space: nowrap;
  }
</style>
</head>
<body>
<main class="canvas">

  <section class="card card-front" aria-label="Business card front">
    <div class="silver-bar top"></div>
    <div class="silver-bar bottom"></div>
    <div class="emblem-fade" role="img" aria-label="Faint brand emblem area"></div>
    <div class="divider"></div>

    <div class="front-brand">
      <div class="wordmark"><span class="dot"></span>HARBORLINE TALENT</div>
      <div class="tagline">READY FOR WHAT COMES NEXT</div>
      <div class="company">HARBORLINE TALENT, INC</div>
    </div>

    <div class="person">
      <h1 class="name">Evan Marlow</h1>
      <p class="title">Manager</p>
      <ul class="contacts">
        <li><span class="icon"><svg viewBox="0 0 10 10"><path d="M2 1l2 2-1 1.2c.6 1.2 1.6 2.2 2.8 2.8L7 6l2 2-1.4 1.4C4.5 9.2.8 5.5.6 2.4z" fill="#fff"/></svg></span>00 4817-2946</li>
        <li><span class="icon"><svg viewBox="0 0 10 10"><rect x="3" y="1" width="4" height="8" rx="1" fill="none" stroke="#fff"/></svg></span>03 615 408 271</li>
        <li><span class="icon"></span>www.quillo-example.com</li>
        <li><span class="icon"></span>www.roomwall-example.com</li>
        <li><span class="icon"><svg viewBox="0 0 10 10"><rect x="1" y="2.5" width="8" height="5" fill="none" stroke="#fff"/><path d="M1 2.5l4 3 4-3" fill="none" stroke="#fff"/></svg></span>evanmarlow@mailbox-example.com</li>
        <li><span class="icon"><svg viewBox="0 0 10 10"><circle cx="5" cy="5" r="3.6" fill="none" stroke="#fff"/><path d="M1.4 5h7.2M5 1.4c-2 2.4-2 4.8 0 7.2M5 1.4c2 2.4 2 4.8 0 7.2" fill="none" stroke="#fff" stroke-width=".7"/></svg></span>www.harborlinetalent-example.com</li>
      </ul>
    </div>
  </section>

  <section class="card card-back" aria-label="Business card back">
    <div class="emblem-fade" role="img" aria-label="Large faded brand emblem area, off centre and bleeding out of frame"></div>
    <div class="back-brand">
      <div class="wordmark"><span class="dot"></span>HARBORLINE TALENT</div>
      <div class="tagline">READY FOR WHAT COMES NEXT</div>
      <div class="company">HARBORLINE TALENT, INC</div>
    </div>
  </section>

</main>
</body>
</html>
```